I will ask the design of the business card

We are looking for business card design of the new company "TORVIK QUANTA WORKS LLC." Based in Azerbaijan.
In case
We are working on Azerbaijan to set up the first exchange of crypto currencies.

The key currency used in exchanges is called "MELDA".
In case
We are doing project to make crypto currency infrastructure.

We provide state-of-the-art technology to the world.

```html
<!DOCTYPE html>
<html lang="en">
<head>
<meta charset="utf-8">
<title>Torvik Quanta Works LLC — Business Card</title>
<link rel="stylesheet" href="https://fonts.googleapis.com/css2?family=Poppins:wght@400;500;600&display=swap">
<style>
  :root{
    --stage:#232323;
    --card-dark:#333333;
    --card-light:#ffffff;
    --brand-blue:#1565c0;
    --ink-dark:#2a2a2a;
    --ink-light:#f2f2f2;
  }
  *{box-sizing:border-box;margin:0;padding:0}
  html,body{width:1200px;height:930px;overflow:hidden;background:var(--stage)}
  body{font-family:"Poppins",sans-serif;position:relative}
  .card{position:absolute;width:520px;height:300px;border-radius:16px;overflow:hidden;background:var(--card-dark)}
  .card--back{left:45px;top:315px}
  .card--front{left:635px;top:315px}
  .brand{position:absolute;display:flex;align-items:center;gap:12px;white-space:nowrap}
  .brand__dot{width:22px;height:22px;border-radius:50%;background:var(--brand-blue)}
  .brand__name{font-weight:400;font-size:22px;letter-spacing:.5px}
  .card--back .brand{left:50%;top:50%;transform:translate(-50%,-50%)}
  .card--back .brand__name{color:var(--ink-light)}
  .card__shape{position:absolute;inset:0}
  .card--front .brand{left:200px;top:48px}
  .card--front .brand__dot{width:18px;height:18px}
  .card--front .brand__name{color:var(--ink-dark);font-size:17px}
  .contact{position:absolute;left:30px;bottom:26px;color:var(--ink-light)}
  .contact__name{color:var(--brand-blue);font-weight:600;font-size:22px;letter-spacing:.5px;line-height:1.1}
  .contact__role{font-size:13px;margin-bottom:10px}
  .contact__address{font-size:12px;line-height:1.45;margin-bottom:8px;padding-left:18px}
  .contact__line{display:flex;align-items:center;gap:8px;font-size:12px;line-height:1.55;padding-left:18px;margin-left:-18px}
  .contact__line svg{width:11px;height:11px;flex:none}
</style>
</head>
<body>
  <section class="card card--back" aria-label="Card back">
    <div class="brand">
      <span class="brand__dot"></span>
      <span class="brand__name">TORVIK QUANTA WORKS LLC</span>
    </div>
  </section>

  <section class="card card--front" aria-label="Card front">
    <svg class="card__shape" viewBox="0 0 520 300" aria-hidden="true">
      <path d="M150 0 Q240 235 520 205 L520 0 Z" fill="#ffffff"/>
      <path d="M138 0 Q228 250 520 210" fill="none" stroke="#1565c0" stroke-width="5"/>
    </svg>
    <div class="brand">
      <span class="brand__dot"></span>
      <span class="brand__name">TORVIK QUANTA WORKS LLC</span>
    </div>
    <div class="contact">
      <p class="contact__name">ELNAR VASKOV</p>
      <p class="contact__role">Director</p>
      <p class="contact__address">AZ1000, 8/21 Ganjavi str.<br>Baku city, Azerbaijan</p>
      <p class="contact__line">
        <svg viewBox="0 0 12 12"><path d="M2 1h3l1 3-1.5 1a6 6 0 0 0 2.5 2.5L8 6l3 1v3a1 1 0 0 1-1 1A9 9 0 0 1 1 2a1 1 0 0 1 1-1z" fill="#1565c0"/></svg>
        615-351-0247
      </p>
      <p class="contact__line">
        <svg viewBox="0 0 12 12"><rect x="1" y="2.5" width="10" height="7" fill="none" stroke="#1565c0" stroke-width="1.2"/><path d="M1 3l5 4 5-4" fill="none" stroke="#1565c0" stroke-width="1.2"/></svg>
        support@melda.technology
      </p>
      <p class="contact__line">
        <svg viewBox="0 0 12 12"><circle cx="6" cy="6" r="5" fill="none" stroke="#1565c0" stroke-width="1.2"/><ellipse cx="6" cy="6" rx="2.2" ry="5" fill="none" stroke="#1565c0" stroke-width="1"/><path d="M1 6h10" stroke="#1565c0" stroke-width="1"/></svg>
        www.guild.melda.technology
      </p>
    </div>
  </section>
</body>
</html>
```